Web Site Design for a Finance (lending) Company

We are opening a new subsidiary that focuses on lending money in the real estate industry. We need a web site designed to represent the business.

The business is lending money to real estate investors. A typical client/borrower will be looking to borrow money to buy a house, renovate it and then sell it at a profit, all within 12 months or less.

Company name is Brevand Finance. Our logo is attached.

Attached is a general outline for the web site. We're working on writing more text for each page but this should give you enough to get started with some ideas.

Competitor web site that I like a lot (as an example): https://quorvelfunding.com/. Many of the general items on this site match what we will need (description of loan programs, FAQ)

Target Market(s)

Real estate investors (generally individuals or small companies with just a few people) who are buying homes, renovating them and then selling them at a profit.

Industry/Entity Type

Finance

Coding

Coded - Design and coding required

Number of Pages Required

5+ page

Colors

Designer to choose colors to be used in the design.

Requirements
Must have
• Minimalist design. Clean lines without too much clutter. Some stock photography is ok but the photos should not be distracting. They should almost fade in to the background so that user can focus on the key information about what our company does instead. We are a finance company, not a design company, so the information about our products will be more interesting to site visitors than the art.
• Some minimalist examples from Snapboard:
• https://www.snapboard-example.com/explore/minimalist-web-design/
Nice to have
• If you search in seekly for "hard money lenders" you will find many examples of web sites from our competition. I have provided a link above to competitor web site that I like a lot.
• I have attached our logo in EPS format. Logo is green. Web site doesn't have to be green but it should be of a color that will work well with the logo.

```html
<!DOCTYPE html>
<html lang="en">
<head>
<meta charset="UTF-8">
<title>Brevand Finance</title>
<link href="https://fonts.googleapis.com/css2?family=Poppins:wght@300;400;500;600&display=swap" rel="stylesheet">
<style>
:root{
  --green:#0f5a3a;
  --green-deep:#1b4d39;
  --ink:#1f1f1f;
  --muted:#8a8a8a;
  --grey-bg:#efefef;
  --grey-line:#d4d4d4;
  --stripe:#8e8f96;
  --white:#ffffff;
}
*{margin:0;padding:0;box-sizing:border-box}
html,body{width:1200px;height:4306px;overflow:hidden;background:var(--white)}
body{font-family:'Poppins',sans-serif;color:var(--ink);position:relative}
.page{position:relative;width:1200px;height:4306px;overflow:hidden}
.abs{position:absolute}
.shape-layer{position:absolute;left:0;top:0}

/* brand */
.brand{display:flex;align-items:center;gap:12px}
.brand-mark{width:30px;height:30px;border:3px solid currentColor}
.brand-name{font-size:22px;font-weight:500;line-height:1.05;width:110px}

/* header */
.site-header{left:158px;top:40px;color:var(--white)}
.main-nav{right:158px;top:60px;display:flex;gap:36px}
.main-nav a{color:var(--white);text-decoration:none;font-size:13px;font-weight:600;letter-spacing:.5px}
.hero-title{left:0;width:1200px;top:262px;text-align:center;color:var(--white);font-size:36px;font-weight:500;line-height:44px;text-shadow:0 2px 6px rgba(0,0,0,.4)}
.btn{display:inline-block;background:var(--green);color:var(--white);font-size:13px;font-weight:600;letter-spacing:.6px;text-decoration:none;padding:0 34px;height:44px;line-height:44px}
.hero-btn{left:522px;top:372px}
.hero-arrow{top:322px;color:var(--white);font-size:28px}

/* section headers */
.sec-mark{width:40px;height:40px;left:580px;border:3px solid var(--green)}
.sec-title{left:0;width:1200px;text-align:center;font-size:34px;font-weight:500;color:var(--ink)}

.welcome-text{left:200px;width:800px;top:800px;text-align:center;font-size:15px;line-height:25px;color:#555}
.welcome-btn{left:522px;top:920px}

/* loans */
.loan-card{width:384px;height:282px;top:1326px}
.loan-frame{position:absolute;inset:0;border:10px solid var(--grey-line)}
.loan-photo{position:absolute;left:18px;top:18px;right:18px;bottom:0}
.loan-title{width:384px;top:1630px;text-align:center;font-size:30px;font-weight:500}
.loan-text{width:384px;top:1700px;text-align:center;font-size:12px;line-height:20px;color:var(--muted)}

/* reasons */
.reason{width:240px}
.reason-icon{width:56px;height:56px;border:2px solid #333;display:flex;align-items:center;justify-content:center}
.reason-label{margin-top:14px;font-size:15px;font-weight:600;padding-bottom:10px;border-bottom:1px solid #ccc;width:72px;white-space:nowrap}
.reason-text{margin-top:22px;font-size:12px;line-height:19px;color:var(--muted)}

/* testimonials */
.testimonial-title{color:var(--white)}
.avatar{left:298px;top:2988px;width:156px;height:156px;border-radius:50%;border:5px solid var(--white);background:linear-gradient(160deg,#d9d9d9,#9c9c9c)}
.quote-name{left:502px;top:3010px;color:var(--white);font-size:16px;font-weight:500}
.quote-text{left:502px;top:3055px;width:480px;color:#e8efe9;font-size:13px;line-height:22px}

/* members */
.member-badge{top:3548px;height:92px;border-radius:8px;background:#8d8d8d}

/* footer */
.footer-brand{left:158px;top:3790px;color:var(--green)}
.social{left:712px;top:3822px;display:flex;align-items:center;gap:10px;font-size:13px;font-weight:600;color:var(--green)}
.social-dot{width:26px;height:26px;border-radius:50%;background:#7c7c7c}
.social-dot.first{background:var(--green)}
.foot-col h4{font-size:14px;font-weight:600;color:var(--green);margin-bottom:22px}
.foot-col li{list-style:none;font-size:13px;line-height:28px;color:#333}
.contact-box{left:537px;top:3892px;width:488px;height:327px;background:var(--white);border:1px solid #e1e1e1;padding:22px 24px}
.contact-box h4{font-size:14px;font-weight:600;color:var(--green);padding-bottom:10px;border-bottom:1px solid #e3e3e3}
.field{position:absolute;font-size:11px;color:#9a9a9a;border-bottom:1px solid #e3e3e3;height:28px;line-height:28px}
.send{position:absolute;left:24px;top:270px;height:36px;line-height:36px;padding:0 24px;font-size:12px}
.copyright{left:0;width:1200px;top:4268px;text-align:center;font-size:13px;font-weight:600;color:#333}
.back-top{right:18px;top:4270px;font-size:11px;color:#888}
</style>
</head>
<body>
<div class="page">

<!-- background shapes -->
<svg class="shape-layer" width="1200" height="4306" viewBox="0 0 1200 4306" aria-hidden="false">
  <defs>
    <linearGradient id="heroSky" x1="0" y1="0" x2="0" y2="1">
      <stop offset="0" stop-color="#2342b5"/>
      <stop offset="0.45" stop-color="#3f5ea8"/>
      <stop offset="0.75" stop-color="#6b5a4e"/>
      <stop offset="1" stop-color="#3a3128"/>
    </linearGradient>
    <linearGradient id="greenHouse" x1="0" y1="0" x2="1" y2="1">
      <stop offset="0" stop-color="#1f5a43"/>
      <stop offset="1" stop-color="#163f30"/>
    </linearGradient>
  </defs>
  <g role="img" aria-label="Photo of a modern two-storey house at dusk with warm window lights">
    <rect x="0" y="0" width="1200" height="600" fill="url(#heroSky)"/>
  </g>
  <polygon points="0,430 600,548 600,582 0,476" fill="var(--green)"/>
  <polygon points="0,476 600,582 1200,470 1200,640 0,640" fill="var(--white)"/>

  <polygon points="0,1062 770,1020 1200,1068 1200,1800 430,1950 0,1900" fill="var(--grey-bg)"/>
  <polygon points="750,1818 1200,1778 1200,1816" fill="var(--stripe)"/>

  <g role="img" aria-label="Faded photo of a modern glass building under a green tint">
    <polygon points="0,2830 860,2712 1200,2756 1200,3040 430,3272 0,3118" fill="url(#greenHouse)"/>
  </g>

  <polygon points="0,3762 1200,3716 1200,4248 0,4248" fill="var(--grey-bg)"/>
</svg>

<!-- header -->
<div class="abs site-header brand">
  <span class="brand-mark"></span>
  <span class="brand-name">Brevand Finance</span>
</div>
<nav class="abs main-nav">
  <a href="#">HOME</a><a href="#">ABOUT US</a><a href="#">LOANS</a><a href="#">RESOURCES</a><a href="#">CONTACT US</a>
</nav>
<span class="abs hero-arrow" style="left:80px">&#8249;</span>
<span class="abs hero-arrow" style="left:1104px">&#8250;</span>
<h1 class="abs hero-title">Local real estate experts lending<br>to local real estate investors</h1>
<a class="abs btn hero-btn" href="#">LEARN MORE</a>

<!-- welcome -->
<span class="abs sec-mark" style="top:650px"></span>
<h2 class="abs sec-title" style="top:712px">Welcome to Brevand Finance</h2>
<p class="abs welcome-text">Brevand Finance is a local business with local knowledge and strong industry relationships. A partner with a wide network who offers value added services. Brevand has an established pool of experienced investors available for your real estate investment needs</p>
<a class="abs btn welcome-btn" href="#">READ MORE</a>

<!-- loans -->
<span class="abs sec-mark" style="top:1128px"></span>
<h2 class="abs sec-title" style="top:1184px">Loans offered</h2>
<div class="abs loan-card" style="left:190px">
  <div class="loan-frame"></div>
  <div class="loan-photo" role="img" aria-label="Black and white photo of a hand holding a small house model" style="background:linear-gradient(135deg,#f4f4f4,#9a9a9a 55%,#3d3d3d)"></div>
</div>
<div class="abs loan-card" style="left:626px">
  <div class="loan-frame"></div>
  <div class="loan-photo" role="img" aria-label="Black and white photo of commercial city towers" style="background:linear-gradient(135deg,#fafafa,#c2c2c2 50%,#6f6f6f)"></div>
</div>
<h3 class="abs loan-title" style="left:190px">Fix and Flip</h3>
<h3 class="abs loan-title" style="left:626px">Commercial</h3>
<p class="abs loan-text" style="left:190px">Short term funding to buy a house, renovate it and sell it at a profit within twelve months. Fast closings, flexible draws and clear terms built for active investors who work on a tight schedule.</p>
<p class="abs loan-text" style="left:626px">Financing for small commercial properties, mixed use buildings and rentals. We review each deal on its merits and structure a loan that fits your plan, timeline and exit strategy.</p>

<!-- why borrow -->
<span class="abs sec-mark" style="top:2004px"></span>
<h2 class="abs sec-title" style="top:2066px">Why borrow from Brevand</h2>

<div class="abs reason" style="left:172px;top:2190px">
  <div class="reason-icon"><svg width="30" height="30" viewBox="0 0 30 30" fill="none" stroke="#333" stroke-width="2"><circle cx="15" cy="12" r="8"/><path d="M10 19l-2 9 7-4 7 4-2-9"/></svg></div>
  <div class="reason-label">Experts</div>
  <p class="reason-text">Our team has years of local lending work and knows what a good deal looks like.</p>
</div>
<div class="abs reason" style="left:465px;top:2190px">
  <div class="reason-icon"><svg width="30" height="30" viewBox="0 0 30 30" fill="none" stroke="#333" stroke-width="2"><rect x="3" y="5" width="24" height="20"/><path d="M9 17l4 4 8-9"/></svg></div>
  <div class="reason-label">Fast Approval</div>
  <p class="reason-text">Simple application and quick decisions so you can close before someone else does.</p>
</div>
<div class="abs reason" style="left:758px;top:2190px">
  <div class="reason-icon"><svg width="30" height="30" viewBox="0 0 30 30" fill="none" stroke="#333" stroke-width="2"><circle cx="15" cy="9" r="5"/><path d="M5 27c1-7 19-7 20 0"/></svg></div>
  <div class="reason-label">Professional</div>
  <p class="reason-text">Clear paperwork, honest answers and steady communication from start to payoff.</p>
</div>
<div class="abs reason" style="left:172px;top:2438px">
  <div class="reason-icon"><svg width="30" height="30" viewBox="0 0 30 30" fill="none" stroke="#333" stroke-width="2"><path d="M3 16l6-6 6 5 6-5 6 6-12 9z"/></svg></div>
  <div class="reason-label">A Partner</div>
  <p class="reason-text">We support your project with a network of trusted contractors and agents nearby.</p>
</div>
<div class="abs reason" style="left:465px;top:2438px">
  <div class="reason-icon"><svg width="30" height="30" viewBox="0 0 30 30" fill="none" stroke="#333" stroke-width="2"><rect x="5" y="4" width="20" height="22"/><path d="M9 10h12M9 15h12M9 20h8"/></svg></div>
  <div class="reason-label">Selective</div>
  <p class="reason-text">We choose solid projects carefully, which keeps our rates fair for every borrower.</p>
</div>
<div class="abs reason" style="left:758px;top:2438px">
  <div class="reason-icon"><svg width="30" height="30" viewBox="0 0 30 30" fill="none" stroke="#333" stroke-width="2"><path d="M4 25h22M7 25V15M13 25V10M19 25V13M25 25V6"/></svg></div>
  <div class="reason-label">Competitive Rates &amp; Fees</div>
  <p class="reason-text">Transparent pricing with no hidden charges and terms that suit short projects.</p>
</div>

<!-- testimonials -->
<span class="abs sec-mark" style="top:2800px;border-color:var(--white)"></span>
<h2 class="abs sec-title testimonial-title" style="top:2862px">Testimonials</h2>
<div class="abs avatar" role="img" aria-label="Portrait photo of the client"></div>
<div class="abs quote-name">Dorian Halvey</div>
<p class="abs quote-text">Brevand funded my second flip in under two weeks. The team was easy to reach, the draws arrived on time and the whole process felt simple. I will be back for my next house and recommend them to other investors.</p>

<!-- members -->
<span class="abs sec-mark" style="top:3366px"></span>
<h2 class="abs sec-title" style="top:3428px">Industry Membership Logos</h2>
<div class="abs member-badge" style="left:168px;width:190px"></div>
<div class="abs member-badge" style="left:442px;width:170px"></div>
<div class="abs member-badge" style="left:708px;width:180px"></div>
<div class="abs member-badge" style="left:918px;width:126px"></div>

<!-- footer -->
<div class="abs footer-brand brand">
  <span class="brand-mark"></span>
  <span class="brand-name">Brevand Finance</span>
</div>
<div class="abs social">
  <span>Social Links</span>
  <span class="social-dot first"></span><span class="social-dot"></span><span class="social-dot"></span><span class="social-dot"></span><span class="social-dot"></span><span class="social-dot"></span>
</div>
<div class="abs foot-col" style="left:158px;top:3912px">
  <h4>Quick Links</h4>
  <ul><li>Home</li><li>About Us</li><li>Loans</li><li>Resources</li><li>Contact Us</li></ul>
</div>
<div class="abs foot-col" style="left:359px;top:3912px">
  <h4>Other Links</h4>
  <ul><li>Terms Of Use</li><li>Privacy Policy</li><li>Help</li><li>Disclaimer</li></ul>
</div>
<form class="abs contact-box">
  <h4>Contact Us</h4>
  <div class="field" style="left:24px;top:68px;width:208px">First Name</div>
  <div class="field" style="left:256px;top:68px;width:208px">Last Name</div>
  <div class="field" style="left:24px;top:110px;width:208px">E-Mail</div>
  <div class="field" style="left:256px;top:110px;width:208px">Phone</div>
  <div class="field" style="left:24px;top:152px;width:440px;height:80px">How can we help? Tell us</div>
  <span class="btn send">SEND</span>
</form>
<p class="abs copyright">&copy; 2017 Company Name &nbsp;|&nbsp; All Rights Reserved</p>
<span class="abs back-top">Up</span>

</div>
</body>
</html>
```